Business Card Design Project For Moving Company

Hello,

We need the business card to be 2 sided and we were thinking to use the logo on the front of the card (see file 1 attached) and the text "logo" (see file 2 attached) in the back of the card. We're looking for a powerful design that will help us build our brand, as our company is new.
We are a full service moving company (no storage) located in San Diego, CA, USA. The design should communicate to our potential customers that we have the highest level of service, customer satisfaction is our number one goal, our team is professional and efficient.

Thank you,

Dorn
Updates

Project Deadline Extended
Reason: We would like to have more time to provide feedback for the designs already submitted. Thank you, Dorn

Industry/Entity Type

Moving Company

Requirements
Must have
• Front of the card must have the following text and logo:
Haulbright, Inc
Residential And Commercial
Local And Long Distance
Address: 7312 Quillmont Rd, #146,
San Diego, CA, 92784
P: 855-372-LIFT (5438)
F: 858-529-4407
info@haul-bright.com
www.haul-bright.com

Back of the card must have the following text and text "logo" (file 2 attached):

The best compliment we can ever receive is a referral from our clients.

```html
<!DOCTYPE html>
<html lang="en">
<head>
<meta charset="utf-8">
<title>Haulbright, Inc — Business Card Back</title>
<link rel="stylesheet" href="https://fonts.googleapis.com/css2?family=Quicksand:wght@500;700&display=swap">
<style>
  :root {
    --charcoal: #333333;
    --paper: #ffffff;
    --accent-red: #f0313a;
    --facet-grey: #f1f1f1;
    --text-light: #ffffff;
  }
  html, body {
    margin: 0;
    padding: 0;
    width: 1200px;
    height: 719px;
    overflow: hidden;
    background: var(--paper);
  }
  .card-back {
    position: relative;
    width: 1200px;
    height: 719px;
    overflow: hidden;
    background: var(--paper);
    font-family: "Quicksand", sans-serif;
  }
  .quote-panel {
    position: absolute;
    left: 0;
    top: 0;
    width: 741px;
    height: 719px;
    background: var(--charcoal);
    border-right: 2px solid var(--accent-red);
    box-sizing: content-box;
  }
  .quote-text {
    position: absolute;
    left: 38px;
    top: 283px;
    margin: 0;
    color: var(--text-light);
    font-weight: 500;
    font-size: 38px;
    line-height: 59px;
    letter-spacing: 0.2px;
  }
  .brand-backdrop {
    position: absolute;
    left: 743px;
    top: 0;
    width: 457px;
    height: 588px;
    background: linear-gradient(135deg, var(--facet-grey) 0%, var(--paper) 45%, var(--facet-grey) 70%, var(--paper) 100%);
  }
  .brand-mark {
    position: absolute;
    left: 743px;
    top: 0;
    width: 457px;
    height: 588px;
    display: flex;
    align-items: center;
    justify-content: center;
    gap: 14px;
  }
  .brand-square {
    width: 26px;
    height: 26px;
    background: var(--accent-red);
  }
  .brand-name {
    color: var(--accent-red);
    font-weight: 700;
    font-size: 50px;
    letter-spacing: 0.5px;
  }
  .accent-band {
    position: absolute;
    left: 0;
    top: 588px;
    width: 1200px;
    height: 52px;
    background: var(--accent-red);
  }
</style>
</head>
<body>
  <main class="card-back">
    <section class="quote-panel">
      <p class="quote-text">The best compliment<br>we can ever receive<br>is a referral from our clients.</p>
    </section>
    <div class="brand-backdrop" role="img" aria-label="Faint light grey angular facets decorating the white background"></div>
    <div class="brand-mark">
      <span class="brand-square"></span>
      <span class="brand-name">Haulbright</span>
    </div>
    <div class="accent-band"></div>
  </main>
</body>
</html>
```